Bref créative |
Jewelry and Home ware website | ||
Studio Kelvara | ||
Jewelry | ||
www.studiokelvara.example | ||
Studio Kelvara is a new company which is just about to launch to the public. Studio Kelvara is a line of handmade jewelry and home ware made with semi precious materials. All pieces are designed and made by me (kela) Rosalind Theda Quarrington. At the moment the brand is very small and the website will be primary used as an online catalogue, eventually hoping to start online buying. | ||
Clean and simple designs, nothing to distract from pieces. |
Clean/Simple Conservative Elegant Traditional Feminine |
Browns | ||
Beiges /Off Whites | ||
Natural tones | ||
left side | ||
View logo on company url. | ||

```html
<!DOCTYPE html>
<html lang="en">
<head>
<meta charset="utf-8">
<title>Studio Kelvara — Jewelry and Home ware</title>
<link rel="stylesheet" href="https://fonts.googleapis.com/css2?family=Arimo:wght@400;700&family=Great+Vibes&display=swap">
<style>
  :root {
    --beige: #e8d4b9;
    --beige-light: #f1e3cf;
    --gold-light: #f6d596;
    --gold: #d9a24f;
    --gold-deep: #9c6320;
    --ink: #3a2414;
    --frame: #b48a5c;
    --pale: #e9dccb;
    --muted: #c3a98a;
  }
  * { box-sizing: border-box; margin: 0; padding: 0; }
  html, body { width: 1200px; height: 900px; overflow: hidden; }
  body {
    position: relative;
    background: var(--beige);
    font-family: "Arimo", Arial, sans-serif;
    color: var(--ink);
  }
  .backdrop { position: absolute; inset: 0; }

  .search {
    position: absolute; left: 54px; top: 15px; width: 183px; height: 30px;
    border: 1.5px solid var(--ink); border-radius: 4px; background: var(--beige-light);
    font-size: 12px; color: #7d6a58; padding: 7px 8px;
  }
  .search svg { position: absolute; right: 7px; top: 6px; }

  .account-nav {
    position: absolute; right: 40px; top: 20px; white-space: nowrap;
    font-size: 14px; color: var(--ink); display: flex; align-items: baseline; gap: 6px;
  }
  .account-nav .sep { color: #7a5a3d; }
  .account-nav .login { font-size: 21px; font-weight: 700; }

  .gold-text {
    background: linear-gradient(180deg, var(--gold-light) 0%, var(--gold) 55%, var(--gold-deep) 100%);
    -webkit-background-clip: text; background-clip: text; color: transparent;
  }
  .headline-jewelry {
    position: absolute; left: 28px; top: 92px; font-size: 74px; line-height: 1;
    font-weight: 400; letter-spacing: -1px; white-space: nowrap;
  }
  .headline-sub {
    position: absolute; left: 68px; top: 166px; font-size: 27px; color: var(--ink); white-space: nowrap;
  }
  .headline-home {
    position: absolute; left: 298px; top: 128px; font-size: 60px; line-height: 1; white-space: nowrap;
  }

  .feature-photo { position: absolute; left: 560px; top: 120px; width: 540px; height: 420px; }
  .maker-name {
    position: absolute; left: 690px; top: 448px; font-family: "Great Vibes", cursive;
    font-size: 24px; color: #b9a999; white-space: nowrap;
  }
  .collection-new {
    position: absolute; right: 40px; top: 326px; font-size: 46px; line-height: 1;
    color: var(--pale);
  }
  .collection-title {
    position: absolute; right: 40px; top: 378px; font-size: 50px; line-height: 1; white-space: nowrap;
  }

  .brand-mark {
    position: absolute; left: 110px; top: 628px;
    display: flex; align-items: center; gap: 12px; white-space: nowrap;
  }
  .brand-mark .dot { width: 22px; height: 22px; border-radius: 50%; background: var(--ink); flex: none; }
  .brand-mark .name { font-size: 30px; color: var(--ink); }

  .product {
    position: absolute; border: 4px solid var(--frame);
    box-shadow: 0 0 0 1px #5c3a1e;
  }
  .product .photo { width: 100%; height: 100%; }
  .product .details {
    position: absolute; right: -6px; bottom: -12px; width: 82px; height: 22px;
    border-radius: 6px; background: #3a2414; border: 1px solid #9a7753;
    color: #f1e3cf; font-size: 12px; text-align: center; line-height: 20px;
  }
  .p1 { left: 505px; top: 568px; width: 190px; height: 147px; }
  .p2 { left: 722px; top: 561px; width: 205px; height: 164px; }
  .p3 { left: 954px; top: 568px; width: 193px; height: 147px; }
  .p1 .photo { background: linear-gradient(160deg, #fbf7f1, #d9d2c6); }
  .p2 .photo { background: radial-gradient(circle at 50% 58%, #f2b45a 0%, #8a4b16 25%, #2a1608 65%); }
  .p3 .photo { background: linear-gradient(160deg, #ffffff, #cfcac4); }

  .pager {
    position: absolute; left: 724px; top: 756px; display: flex; align-items: center; gap: 11px;
    font-size: 17px; color: var(--muted);
  }
  .pager .current { color: var(--pale); font-size: 21px; font-weight: 700; }

  .site-nav {
    position: absolute; left: 68px; top: 838px; font-size: 15px; color: var(--ink);
    display: flex; align-items: baseline; gap: 6px; white-space: nowrap;
  }
  .site-nav .strong { font-size: 19px; font-weight: 700; }
  .service-nav {
    position: absolute; right: 40px; top: 838px; font-size: 14px; color: #cbb192;
    display: flex; align-items: baseline; gap: 6px; white-space: nowrap;
  }
  .service-nav .strong { font-size: 19px; font-weight: 700; color: var(--gold); }
</style>
</head>
<body>
  <svg class="backdrop" width="1200" height="900" viewBox="0 0 1200 900" aria-hidden="true">
    <defs>
      <linearGradient id="panelShade" x1="0" y1="0" x2="1" y2="1">
        <stop offset="0" stop-color="#4a2c15"/>
        <stop offset="1" stop-color="#2c180a"/>
      </linearGradient>
    </defs>
    <path d="M280 54 H1200 V900 H350 C310 840 270 770 310 700 C370 600 510 570 500 470 C490 360 300 310 285 180 Z"
          fill="url(#panelShade)" stroke="#c9955a" stroke-width="3"/>
  </svg>

  <div class="search">Search entire store here ...
    <svg width="16" height="16" viewBox="0 0 16 16"><circle cx="6.5" cy="6.5" r="4.5" fill="none" stroke="#3a2414" stroke-width="1.6"/><line x1="10" y1="10" x2="14.5" y2="14.5" stroke="#3a2414" stroke-width="1.8"/></svg>
  </div>

  <nav class="account-nav">
    <span>My Account</span><span class="sep">|</span><span>My Wishlist</span><span class="sep">|</span><span>My Cart</span><span class="sep">|</span><span>Checkout</span><span class="sep">|</span><span class="login">Log In</span>
  </nav>

  <h1 class="headline-jewelry gold-text">Jewelry</h1>
  <p class="headline-sub">Studio Kelvara</p>
  <p class="headline-home gold-text">and Home ware</p>

  <svg class="feature-photo" viewBox="0 0 540 420" role="img" aria-label="Photograph of a lit candle in a lattice holder glowing in the dark">
    <defs>
      <radialGradient id="glow" cx="0.5" cy="0.5" r="0.5">
        <stop offset="0" stop-color="#f8c46a"/>
        <stop offset="0.22" stop-color="#b86a22"/>
        <stop offset="0.6" stop-color="#6a3c18" stop-opacity="0.7"/>
        <stop offset="1" stop-color="#3a2010" stop-opacity="0"/>
      </radialGradient>
    </defs>
    <ellipse cx="250" cy="210" rx="240" ry="205" fill="url(#glow)"/>
  </svg>
  <p class="maker-name">Rosalind Theda Quarrington</p>

  <p class="collection-new">New</p>
  <p class="collection-title gold-text">Collection</p>

  <div class="brand-mark"><span class="dot"></span><span class="name">Studio Kelvara</span></div>

  <div class="product p1"><div class="photo" role="img" aria-label="Photograph of a beaded collar necklace"></div><span class="details">Details</span></div>
  <div class="product p2"><div class="photo" role="img" aria-label="Photograph of a candle holder with lit candle"></div><span class="details">Details</span></div>
  <div class="product p3"><div class="photo" role="img" aria-label="Photograph of a silver ring"></div><span class="details">Details</span></div>

  <div class="pager">
    <svg width="20" height="20" viewBox="0 0 20 20"><circle cx="10" cy="10" r="8.5" fill="none" stroke="#c3a98a" stroke-width="1.5"/><path d="M12 6 L7.5 10 L12 14 Z" fill="#c3a98a"/></svg>
    <span>1</span><span>2</span><span class="current">3</span><span>4</span><span>5</span><span>6</span>
    <svg width="20" height="20" viewBox="0 0 20 20"><circle cx="10" cy="10" r="9" fill="#d9a24f"/><path d="M8 6 L12.5 10 L8 14 Z" fill="#2e1a0c"/></svg>
  </div>

  <nav class="site-nav"><span>Home</span><span>|</span><span>About Me</span><span>|</span><span class="strong">Catalog</span></nav>
  <nav class="service-nav"><span>Gift cards</span><span>|</span><span>Delivery &amp; Returns</span><span>|</span><span class="strong">Newsletter</span></nav>
</body>
</html>
```